Psychotherapy, Life Coaching, Writer, Motivational Speaker

I am a psychotherapist, life coach, writer and speaker on health and wellness issues. I am a humanist - who believes that we are born to self-actualize - but life - changes that course. That we develop armor and coping mechanisms that divert our growth. I help people examine their road blocks to happiness. My business is unique in that I do concierge therapy. I work intensively - with multi-day sessions, I work internationally through tele-therapy - and traditionally - in an office space. My work is tailored to your needs.

Target Market(s)

Broad

Industry/Entity Type

Health

Contact Information for Business Card

Listen To Grow
Sam Virelle
482 East 23rd Street
New York, NY 10027
(305) 418-7302

Requirements
Must have
• Clean lines... not too busy...
• FB page listing: Listen To Grow
• my Web page: www.listentogrow-example.com
Nice to have
• I would love to be able to list the services: Psychotherapist, Life Coach, Motivational Speaker and Writer - but also don't want a crazy crowded card. Feel free to use the back for description.
Should not have
• Stay away from corny imagery - lotus flowers, zen, lily pond, clouds.

```html
<!DOCTYPE html>
<html lang="en">
<head>
<meta charset="utf-8">
<title>Listen To Grow — Business Card</title>
<link rel="stylesheet" href="https://fonts.googleapis.com/css2?family=Lato:wght@400;700&display=swap">
<style>
  :root {
    --brand-blue: #4a81c4;
    --ink: #111111;
    --paper: #ffffff;
    --panel: #000000;
  }
  html, body {
    margin: 0;
    padding: 0;
    overflow: hidden;
    background: var(--paper);
  }
  .card {
    position: relative;
    width: 1200px;
    height: 758px;
    overflow: hidden;
    background: var(--paper);
    font-family: "Lato", Arial, sans-serif;
    color: var(--ink);
  }
  .card-shape {
    position: absolute;
    inset: 0;
    width: 1200px;
    height: 758px;
  }
  .brand-name {
    position: absolute;
    left: 97px;
    top: 161px;
    margin: 0;
    font-size: 50px;
    font-weight: 700;
    color: var(--brand-blue);
    letter-spacing: 0.2px;
    white-space: nowrap;
  }
  .contact-list {
    position: absolute;
    left: 90px;
    top: 296px;
    margin: 0;
    padding: 0;
    list-style: none;
    font-size: 33px;
    line-height: 41px;
  }
  .contact-item {
    display: flex;
    align-items: center;
    white-space: nowrap;
  }
  .contact-icon {
    width: 24px;
    height: 24px;
    margin-right: 7px;
    flex: none;
    fill: var(--brand-blue);
  }
  .social-square {
    width: 22px;
    height: 22px;
    margin-right: 8px;
    border-radius: 3px;
    background: var(--brand-blue);
    flex: none;
  }
  .address {
    position: absolute;
    left: 96px;
    top: 541px;
    margin: 0;
    font-style: normal;
    font-size: 30px;
    line-height: 38px;
    white-space: nowrap;
  }
  .person {
    position: absolute;
    right: 95px;
    top: 344px;
    text-align: right;
    color: var(--paper);
    white-space: nowrap;
  }
  .person-name {
    margin: 0;
    font-size: 33px;
  }
  .person-name strong {
    font-size: 40px;
    font-weight: 700;
    color: var(--brand-blue);
  }
  .person-title {
    margin: 2px 0 0;
    font-size: 33px;
  }
</style>
</head>
<body>
  <main class="card">
    <svg class="card-shape" viewBox="0 0 1122 708" preserveAspectRatio="none" aria-hidden="true">
      <path fill="var(--brand-blue)" d="M680,0 C600,120 565,260 580,380 C588,440 600,480 612,505 L1122,505 L1122,0 Z"/>
      <path fill="var(--panel)" d="M792,0 C680,100 600,260 595,420 C593,540 650,640 702,708 L1122,708 L1122,0 Z"/>
    </svg>

    <h1 class="brand-name">Listen To Grow</h1>

    <ul class="contact-list">
      <li class="contact-item">
        <svg class="contact-icon" viewBox="0 0 24 24" aria-hidden="true">
          <path d="M2,9 C2,5 7,4 12,4 C17,4 22,5 22,9 L22,10 L17,10 L17,7.5 L7,7.5 L7,10 L2,10 Z"/>
          <path d="M6,11 L8,9 L16,9 L18,11 L20,19 L4,19 Z"/>
          <rect x="9" y="12" width="6" height="5" fill="#ffffff"/>
        </svg>
        (305) 418-7302
      </li>
      <li class="contact-item">
        <svg class="contact-icon" viewBox="0 0 24 24" aria-hidden="true">
          <rect x="1" y="5" width="22" height="15" rx="1"/>
          <path d="M2,6 L12,14 L22,6" fill="none" stroke="#ffffff" stroke-width="1.6"/>
          <path d="M2,19 L9,12 M22,19 L15,12" fill="none" stroke="#ffffff" stroke-width="1.2"/>
        </svg>
        svirelle.studio@example.com
      </li>
      <li class="contact-item">
        <svg class="contact-icon" viewBox="0 0 24 24" aria-hidden="true">
          <circle cx="12" cy="12" r="11"/>
          <g fill="none" stroke="#ffffff" stroke-width="1.3">
            <ellipse cx="12" cy="12" rx="5" ry="11"/>
            <line x1="12" y1="1" x2="12" y2="23"/>
            <line x1="1" y1="12" x2="23" y2="12"/>
            <path d="M3,6.5 H21 M3,17.5 H21"/>
          </g>
        </svg>
        www.listentogrow-example.com
      </li>
      <li class="contact-item">
        <span class="social-square" aria-hidden="true"></span>
        Listen To Grow
      </li>
    </ul>

    <address class="address">
      482 East 23rd Street<br>
      New York, NY 10027
    </address>

    <div class="person">
      <p class="person-name"><strong>Sam Virelle</strong> LMHC, NCC</p>
      <p class="person-title">Psychotherapist.</p>
    </div>
  </main>
</body>
</html>
```